Need professional looking PowerPoint Slide

Content is all created but it looks lame. I need it to look good. Please modify attached slide. Logo needs to stay on it. Green color should be used as well.
Industry/Entity Type
Health Care
Font styles to use
Serif
Requirements
Must have
- all original content contained
Nice to have
- additional design elements such as photo(s)

```html
<!DOCTYPE html>
<html lang="en">
<head>
<meta charset="utf-8">
<title>Stage to a New Care Model</title>
<link rel="stylesheet" href="https://fonts.googleapis.com/css2?family=Montserrat:wght@300;400;700&family=Fira+Sans+Extra+Condensed:wght@700;800&family=Open+Sans:wght@300;400;600;700&display=swap">
<style>
  :root {
    --bg: #e8e8e8;
    --panel: #f3f3f3;
    --box: #ececec;
    --ink: #111111;
    --green: #3f9d35;
    --green-light: #7ac943;
    --green-dark: #1f8a3a;
    --rail: #58b04a;
    --white: #ffffff;
  }
  * { box-sizing: border-box; margin: 0; padding: 0; }
  html, body { width: 1200px; height: 1000px; overflow: hidden; background: var(--bg); }
  .slide { position: relative; width: 1200px; height: 1000px; background: linear-gradient(180deg, #ececec 0%, #e6e6e6 100%); font-family: "Open Sans", Arial, sans-serif; color: var(--ink); }

  .hero-photo { position: absolute; right: 0; top: 0; width: 270px; height: 232px; background: linear-gradient(90deg, rgba(236,236,236,0) 0%, #dfe6ea 35%, #f4f6f7 70%, #e2e8ec 100%); }

  .goals-title { position: absolute; left: 58px; top: 34px; font-family: "Montserrat", Verdana, sans-serif; font-weight: 700; font-size: 25px; letter-spacing: 0.3px; }
  .goals-list { position: absolute; left: 96px; top: 88px; list-style: none; font-family: "Montserrat", Verdana, sans-serif; font-weight: 400; font-size: 27px; line-height: 34.5px; }
  .goals-list li::before, .col-list li::before { content: ""; display: inline-block; width: 10px; height: 10px; border-radius: 50%; background: var(--green); margin-right: 8px; vertical-align: middle; position: relative; top: -3px; }

  .stage-panel { position: absolute; left: 60px; top: 233px; width: 1080px; height: 285px; background: linear-gradient(180deg, #fbfbfb 0%, #f0f0f0 100%); border: 1px solid #dcdcdc; border-radius: 18px; }
  .stage-title { position: absolute; left: 386px; top: 246px; font-family: "Fira Sans Extra Condensed", "Arial Narrow", sans-serif; font-weight: 800; font-size: 30px; }
  .launch-title { position: absolute; left: 920px; top: 254px; width: 220px; text-align: center; font-family: Arial, Helvetica, sans-serif; font-weight: 700; font-size: 27px; line-height: 31px; }
  .rail { position: absolute; left: 70px; top: 367px; width: 940px; height: 8px; background: var(--rail); }
  .step { position: absolute; top: 346px; width: 191px; height: 51px; border-radius: 7px; background: linear-gradient(180deg, #8ed05a 0%, #5cb443 45%, #3d9b35 100%); color: var(--white); text-align: center; line-height: 51px; font-family: "Fira Sans Extra Condensed", "Arial Narrow", sans-serif; font-weight: 700; font-size: 27px; text-shadow: 0 1px 2px rgba(0,0,0,0.35); }
  .step-research { left: 117px; } .step-exploration { left: 415px; } .step-execution { left: 713px; }
  .node { position: absolute; top: 355px; width: 32px; height: 32px; border-radius: 50%; background: radial-gradient(circle at 40% 30%, #9ede6d 0%, #46a83a 60%, #2e8a2e 100%); }
  .launch-badge { position: absolute; left: 980px; top: 325px; width: 92px; height: 92px; }
  .step-notes { position: absolute; top: 417px; width: 218px; height: 83px; background: var(--box); display: flex; align-items: center; justify-content: center; text-align: center; font-weight: 600; font-size: 15px; line-height: 19.5px; }
  .notes-research { left: 103px; } .notes-exploration { left: 400px; } .notes-execution { left: 701px; }

  .column { position: absolute; top: 548px; width: 274px; height: 268px; background: var(--panel); }
  .column:nth-of-type(1) { left: 28px; }
  .col-1 { left: 28px; } .col-2 { left: 318px; } .col-3 { left: 609px; } .col-4 { left: 899px; }
  .col-head { height: 50px; background: linear-gradient(180deg, #9ad76c 0%, #5ab545 40%, #3a9c36 100%); color: var(--white); text-align: center; line-height: 52px; font-family: "Fira Sans Extra Condensed", "Arial Narrow", sans-serif; font-weight: 700; font-size: 24px; text-shadow: 0 1px 2px rgba(0,0,0,0.35); }
  .col-list { list-style: none; padding: 20px 6px 0 6px; font-family: "Open Sans", Arial, sans-serif; font-weight: 300; font-size: 22px; line-height: 29.5px; }
  .col-list li { padding-left: 20px; text-indent: -18px; }
  .col-list li::before { width: 7px; height: 7px; margin-right: 3px; top: -2px; }

  .footer-arc { position: absolute; left: 78px; top: 832px; width: 1046px; height: 20px; }
  .footer { position: absolute; left: 0; top: 851px; width: 1200px; height: 149px; background: linear-gradient(90deg, #e4e4e4 0%, #fafafa 50%, #e4e4e4 100%); }
  .brand { position: absolute; left: 456px; top: 866px; display: flex; align-items: center; gap: 18px; }
  .brand-dot { width: 68px; height: 68px; border-radius: 50%; background: var(--green); }
  .brand-name { font-family: "Open Sans", Arial, sans-serif; font-weight: 300; font-size: 60px; color: var(--ink); letter-spacing: -1px; }
  .brand-tagline { position: absolute; left: 542px; top: 956px; width: 202px; border-top: 1px solid #9a9a9a; padding-top: 3px; font-family: Arial, sans-serif; font-size: 8.5px; font-weight: 700; text-align: center; }
</style>
</head>
<body>
<main class="slide">
  <div class="hero-photo" role="img" aria-label="Photo of a physician in a white coat with a stethoscope, arms crossed"></div>

  <h1 class="goals-title">Goals: Assist in Renewing/Redefining your Value Proposition:</h1>
  <ul class="goals-list">
    <li>Change your healthcare delivery model</li>
    <li>Redefine the way you engage with patients/families</li>
    <li>Take new steps in achieving the Triple-Aim plus One</li>
  </ul>

  <section class="stage-panel" aria-label="Stage to a new care model"></section>
  <h2 class="stage-title">STAGE TO A NEW CARE MODEL</h2>
  <h2 class="launch-title">NEW SERVICE LAUNCH</h2>
  <div class="rail"></div>
  <div class="step step-research">RESEARCH</div>
  <div class="node" style="left:347px"></div>
  <div class="step step-exploration">EXPLORATION</div>
  <div class="node" style="left:643px"></div>
  <div class="step step-execution">EXECUTION</div>
  <svg class="launch-badge" viewBox="0 0 92 92" aria-hidden="true">
    <defs>
      <radialGradient id="badgeFill" cx="40%" cy="30%" r="75%">
        <stop offset="0" stop-color="#9ede6d"/>
        <stop offset="0.6" stop-color="#3fa13a"/>
        <stop offset="1" stop-color="#237d2c"/>
      </radialGradient>
    </defs>
    <circle cx="46" cy="46" r="44" fill="url(#badgeFill)" stroke="#ffffff" stroke-width="2"/>
    <polygon fill="#ffffff" points="46,14 54,37 78,37 59,51 66,74 46,60 26,74 33,51 14,37 38,37"/>
  </svg>
  <div class="step-notes notes-research">Market Study<br>Macro Issues<br>Data Analytics</div>
  <div class="step-notes notes-exploration">Etnography<br>Solution Proposal</div>
  <div class="step-notes notes-execution">Service Creation<br>Verification &amp; Validation</div>

  <section class="column col-1">
    <h3 class="col-head">New Value Proposition</h3>
    <ul class="col-list">
      <li>Population Health</li>
      <li>Redesign continuum of care from fee-for-service based model to at-risk</li>
      <li>Bundled Payment</li>
    </ul>
  </section>
  <section class="column col-2">
    <h3 class="col-head">New Business Model</h3>
    <ul class="col-list">
      <li>Hub &amp; Spoke</li>
      <li>Extend from Ambulatory to Integrated System</li>
      <li>Health plans</li>
    </ul>
  </section>
  <section class="column col-3">
    <h3 class="col-head">New Service Line</h3>
    <ul class="col-list">
      <li>Orthopedics</li>
      <li>Oncology</li>
      <li>Cardiology</li>
    </ul>
  </section>
  <section class="column col-4">
    <h3 class="col-head">New Technology</h3>
    <ul class="col-list">
      <li>Smartphone and tablet apps</li>
      <li>EMR</li>
      <li>3T MRI</li>
      <li>Virtual visits</li>
      <li>Telehealth</li>
    </ul>
  </section>

  <svg class="footer-arc" viewBox="0 0 1046 20" preserveAspectRatio="none" aria-hidden="true">
    <path d="M0 20 Q523 -14 1046 20 Z" fill="var(--green-dark)"/>
  </svg>
  <footer class="footer"></footer>
  <div class="brand">
    <span class="brand-dot"></span>
    <span class="brand-name">Clearwell</span>
  </div>
  <div class="brand-tagline">A MERIDIAN HEALTH INSIGHTS COMPANY</div>
</main>
</body>
</html>
```